Aerospace Private Equity Firm Needs Website

We need a website for new private equity fund called Corvin Partners. We buy smaller companies in the aerospace and industrial industries. I have attached some information about the firm. An example of a site we like that is a similar business but focused in a different sector is www.tarnowcare.com. www.quillstonefunds.com is a firm that also invests in aerospace companies.

Industry/Entity Type

Equity

Number of Pages Required

1 page

Colors
0555a3
33a6d7
ec1f27

```html
<!DOCTYPE html>
<html lang="en">
<head>
<meta charset="utf-8">
<title>Corvin Partners</title>
<link href="https://fonts.googleapis.com/css2?family=Source+Sans+3:ital,wght@0,300;0,400;0,600;0,700;1,400;1,600&display=swap" rel="stylesheet">
<style>
:root{
  --navy:#0a3a8c;
  --navy-deep:#062d6e;
  --blue:#0555a3;
  --sky:#33a6d7;
  --red:#ec1f27;
  --ink:#333a45;
  --muted:#8a8f98;
  --light:#f3f3f3;
  --gray-band:#ebecef;
  --footer:#4a4a4a;
  --white:#ffffff;
}
*{box-sizing:border-box;margin:0;padding:0}
html,body{width:1200px;height:3488px;overflow:hidden}
body{font-family:"Source Sans 3",Arial,sans-serif;color:var(--ink);background:var(--white);position:relative}
section,header,footer{position:relative;width:1200px}

/* header */
.site-header{height:100px;background:var(--white)}
.brand{position:absolute;left:70px;top:14px;font-weight:700;font-size:40px;color:var(--navy);letter-spacing:.5px;display:flex;align-items:center;gap:12px}
.brand-dot{width:14px;height:14px;background:var(--red)}
.social{position:absolute;left:940px;top:46px;display:flex;gap:8px}
.social span{width:16px;height:16px;background:#8d8f93;border-radius:2px}
.login{position:absolute;left:1072px;top:44px;width:76px;height:20px;background:var(--navy);color:#fff;font-size:12px;font-weight:600;text-align:center;line-height:20px;border-radius:2px}

.main-nav{height:33px;background:var(--navy-deep);display:flex;padding-left:51px}
.main-nav a{color:#fff;text-decoration:none;font-size:12.5px;font-weight:600;text-transform:uppercase;line-height:33px;padding:0 28px;border-right:1px solid rgba(255,255,255,.25)}
.main-nav a.active{background:var(--red);padding:0 35px}
.main-nav a:last-child{border-right:none}

/* hero */
.hero{height:583px;overflow:hidden}
.hero-bg{position:absolute;inset:0;background:linear-gradient(135deg,#4d6f9e 0%,#264f8d 40%,#16397a 75%,#1a3364 100%)}
.hero-title{position:absolute;top:222px;width:100%;text-align:center;color:#fff;font-size:72px;font-weight:600;letter-spacing:.5px}
.hero-sub{position:absolute;top:312px;width:100%;text-align:center;color:#fff;font-size:37px;font-style:italic}

/* section headings */
.section-title{text-align:center;color:var(--navy);font-size:37px;font-weight:600}
.rule{width:38px;height:3px;background:var(--red);margin:14px auto 0}

/* interests */
.interests{height:440px}
.interests .section-title{position:absolute;top:36px;width:100%}
.interests .rule{position:absolute;top:96px;left:581px;margin:0}
.card{position:absolute;top:131px;width:236px;height:246px;border:1px solid #e3e3e3;background:#fff;text-align:center}
.card svg{margin-top:44px}
.card h3{color:var(--navy);font-size:14px;font-weight:700;margin-top:8px}
.card .rule{width:24px;height:2px;margin:6px auto 0;position:static}
.card p{color:#b4b8be;font-size:13px;line-height:17px;margin:16px 34px 0}
.card .more{display:block;color:var(--navy);font-size:11.5px;font-weight:600;margin-top:14px}
.card .more b{color:var(--red)}

/* about */
.about{height:454px;background:var(--gray-band)}
.about h2{position:absolute;left:167px;top:72px;color:var(--navy);font-size:37px;font-weight:600}
.about .rule{position:absolute;left:167px;top:128px;margin:0}
.about p{position:absolute;left:167px;top:166px;width:470px;font-size:13px;line-height:20px;color:#555b63}
.btn{position:absolute;background:var(--navy);color:#fff;font-size:12.5px;font-weight:600;text-transform:uppercase;display:flex;align-items:center;justify-content:space-between;padding:0 14px 0 18px}
.about .btn{left:167px;top:305px;width:142px;height:33px}
.video{position:absolute;left:633px;top:72px;width:407px;height:272px;background:#fff;padding:10px;box-shadow:0 2px 6px rgba(0,0,0,.12)}
.video-frame{position:relative;width:100%;height:100%;background:linear-gradient(180deg,#6b5c55 0%,#4a3f3b 60%,#151515 100%)}
.video-bar{position:absolute;left:0;right:0;bottom:0;height:18px;background:#111}
.play{position:absolute;left:170px;top:108px}

/* stats */
.stats{height:244px;overflow:hidden}
.stats-bg{position:absolute;inset:0;background:linear-gradient(90deg,#1e4d97 0%,#123d86 50%,#0c3176 100%)}
.stats h2{position:absolute;left:149px;top:88px;color:#fff;font-size:29px;font-weight:400;line-height:36px;text-align:center}
.stat{position:absolute;top:78px;color:#fff;text-align:center;width:140px}
.stat strong{display:block;font-size:44px;font-weight:400;line-height:46px}
.stat span{font-size:20px}
.stat-divider{position:absolute;top:80px;width:2px;height:88px;background:rgba(255,255,255,.7)}

/* team */
.team{height:693px;background:var(--light)}
.team .section-title{position:absolute;top:46px;width:100%}
.team .rule{position:absolute;top:104px;left:581px;margin:0}
.team .lead{position:absolute;top:118px;width:100%;text-align:center;font-size:12px;line-height:16px;color:#777}
.member{position:absolute;top:186px;height:453px;background:#fff}
.member .photo{height:270px}
.member h3{font-size:15px;font-weight:700;color:#222;margin:16px 0 0 26px}
.member .role{font-size:14px;color:#333;margin:2px 0 0 26px}
.member p{font-size:12.5px;line-height:18px;color:#555;margin:16px 22px 0 26px}
.arrow{position:absolute;top:460px}

/* strategy */
.strategy{height:456px}
.strategy-photo{position:absolute;left:0;top:0;width:679px;height:456px;background:linear-gradient(160deg,#6f6a66 0%,#a7a29a 45%,#c9b9a3 70%,#8d7f72 100%)}
.strategy-panel{position:absolute;left:679px;top:0;width:521px;height:456px;background:var(--navy);color:#fff;padding:40px 0 0 47px}
.strategy-panel h2{font-size:38px;font-weight:400}
.strategy-panel .rule{width:38px;margin:14px 0 0}
.strategy-panel h3{font-size:19px;font-weight:600;margin-top:14px}
.strategy-panel .desc{font-size:12.5px;margin-top:2px}
.strategy-panel ul{list-style:none;margin-top:6px}
.strategy-panel li{font-size:12.5px;line-height:18px;padding-left:14px;position:relative}
.strategy-panel li::before{content:"\203A";position:absolute;left:0;top:-2px;font-size:17px;font-weight:700}
.strategy-panel .btn{position:absolute;left:47px;top:388px;width:142px;height:33px;background:transparent;border:1px solid #fff}

/* partners */
.partners{height:430px}
.partners .section-title{position:absolute;top:60px;width:100%}
.partners .rule{position:absolute;top:120px;left:581px;margin:0}
.partners .lead{position:absolute;top:154px;width:100%;text-align:center;font-size:12px;line-height:16px;color:#777}
.partner-row{position:absolute;top:245px;left:100px;width:1000px;display:flex;justify-content:space-between;align-items:center}
.partner{display:flex;align-items:center;gap:8px;font-size:17px;font-weight:700;color:var(--navy)}
.partner i{width:12px;height:12px;background:var(--navy);display:block}

/* footer */
.site-footer{height:55px;background:var(--footer);color:#d0d0d0;font-size:12px;text-align:center;line-height:55px}
</style>
</head>
<body>

<header class="site-header">
  <div class="brand"><span class="brand-dot"></span>Corvin Partners</div>
  <div class="social"><span></span><span></span><span></span><span></span></div>
  <div class="login">LOGIN</div>
</header>

<nav class="main-nav">
  <a class="active" href="#">Home</a>
  <a href="#">About</a>
  <a href="#">Team</a>
  <a href="#">Investments</a>
  <a href="#">Strategy</a>
  <a href="#">Aerospace</a>
  <a href="#">Industrial</a>
  <a href="#">Portfolio Companies</a>
  <a href="#">Press</a>
  <a href="#">Contact</a>
</nav>

<section class="hero">
  <div class="hero-bg" role="img" aria-label="Business team reviewing charts on a tablet"></div>
  <h1 class="hero-title">Partners have a combined</h1>
  <p class="hero-sub">60 years of investing &amp; operating experience</p>
</section>

<section class="interests">
  <h2 class="section-title">Area of Interest</h2>
  <div class="rule"></div>

  <article class="card" style="left:195px">
    <svg width="40" height="40" viewBox="0 0 40 40" fill="none" stroke="#ec1f27" stroke-width="2">
      <circle cx="15" cy="20" r="8"/><circle cx="15" cy="20" r="3"/>
      <path d="M15 9v-3M15 34v-3M4 20h-3M29 20h-3M7 12l-2-2M25 30l-2-2M7 28l-2 2M23 12l2-2"/>
      <circle cx="31" cy="10" r="5"/><circle cx="31" cy="10" r="1.5"/>
    </svg>
    <h3>Industry</h3><div class="rule"></div>
    <p>Corvin will invest in undervalued aerospace and industrial companies.</p>
    <span class="more">Read More <b>&raquo;</b></span>
  </article>

  <article class="card" style="left:491px">
    <svg width="40" height="40" viewBox="0 0 40 40" fill="none" stroke="#ec1f27" stroke-width="2">
      <circle cx="20" cy="6" r="3"/><path d="M16 12h8l-2 14h-4zM13 30h14l2 6H11z"/>
    </svg>
    <h3>Strategy</h3><div class="rule"></div>
    <p>Corvin will invest in undervalued aerospace and industrial companies.</p>
    <span class="more">Read More <b>&raquo;</b></span>
  </article>

  <article class="card" style="left:795px">
    <svg width="40" height="40" viewBox="0 0 40 40" fill="none" stroke="#ec1f27" stroke-width="2">
      <path d="M6 38V10h5v28M11 22l9-6v6l9-6v6l8-5v21H6"/><path d="M8 6c3-3 7-3 10 0s7 3 10 0"/>
    </svg>
    <h3>Industry</h3><div class="rule"></div>
    <p>Corvin will invest in undervalued aerospace and industrial companies.</p>
    <span class="more">Read More <b>&raquo;</b></span>
  </article>
</section>

<section class="about">
  <h2>Corvin Partners</h2>
  <div class="rule"></div>
  <p>Corvin Partners (&ldquo;Corvin&rdquo;) is a Los Angeles, California-based private equity firm formed in 2016 by Principals from Larkfield Associates (LFA). Corvin focuses on lower middle-market control investments in aerospace and industrial companies based in North America. The Corvin team has invested successfully in these sectors over a 10 - year period while at LFA.</p>
  <div class="btn">Read More
    <svg width="10" height="14" viewBox="0 0 10 14"><path d="M2 1l6 6-6 6" fill="none" stroke="#fff" stroke-width="2"/></svg>
  </div>
  <div class="video">
    <div class="video-frame" role="img" aria-label="Video still of a partner speaking about the firm">
      <svg class="play" width="46" height="32" viewBox="0 0 46 32"><rect width="46" height="32" rx="6" fill="#1b1b1b"/><path d="M18 9l12 7-12 7z" fill="#fff"/></svg>
      <div class="video-bar"></div>
    </div>
  </div>
</section>

<section class="stats">
  <div class="stats-bg" role="img" aria-label="Blue-toned office background"></div>
  <h2>We Have 61 Years<br>of Experiences</h2>
  <div class="stat" style="left:614px"><strong>1500</strong><span>Clients</span></div>
  <div class="stat-divider" style="left:760px"></div>
  <div class="stat" style="left:770px"><strong>1255</strong><span>Projects</span></div>
  <div class="stat-divider" style="left:919px"></div>
  <div class="stat" style="left:926px"><strong>18</strong><span>Awards</span></div>
</section>

<section class="team">
  <h2 class="section-title">Team</h2>
  <div class="rule"></div>
  <p class="lead">Corvin Partners have had P&amp;L responsibilities in LMM Companies - invest<br>with an operational mindset</p>

  <svg class="arrow" style="left:40px" width="16" height="26" viewBox="0 0 16 26"><path d="M13 2L3 13l10 11" fill="none" stroke="#0a3a8c" stroke-width="3"/></svg>

  <article class="member" style="left:149px;width:274px">
    <div class="photo" role="img" aria-label="Portrait of Marta Elvessen" style="background:linear-gradient(180deg,#e6e3de 0%,#c9b19a 55%,#9a8f86 100%)"></div>
    <h3>Marta Elvessen</h3>
    <div class="role">Founder</div>
    <p>15 Years of International experience in product marketing, sales &amp; distribution in the aerospace and industrial sectors</p>
  </article>

  <article class="member" style="left:458px;width:270px">
    <div class="photo" role="img" aria-label="Portrait of Dale Hurst" style="background:linear-gradient(180deg,#b9b6b2 0%,#d4c4b6 50%,#3a3a3c 100%)"></div>
    <h3>Dale Hurst</h3>
    <div class="role">CEO of Tenmark Products</div>
    <p>CEO for 20+ years.Successfully integrated 4 add-on acquisitions.Former Chairman of the Kiln Materials Institute. MBA from Ridgeview University</p>
  </article>

  <article class="member" style="left:763px;width:270px">
    <div class="photo" role="img" aria-label="Portrait of Glen Ashby" style="background:linear-gradient(180deg,#c6ccd4 0%,#c9a790 50%,#6d7b95 100%)"></div>
    <h3>Glen Ashby</h3>
    <div class="role">Founder of Ashby Aerospace</div>
    <p>Grew up working for family's aerospace business. Started Ashby Aerospace, now a critical supplier of high pressure fittings to OEM's</p>
  </article>

  <svg class="arrow" style="left:1146px" width="16" height="26" viewBox="0 0 16 26"><path d="M3 2l10 11L3 24" fill="none" stroke="#0a3a8c" stroke-width="3"/></svg>
</section>

<section class="strategy">
  <div class="strategy-photo" role="img" aria-label="Team planning with sticky notes and documents on a table"></div>
  <div class="strategy-panel">
    <h2>Investment Strategy</h2>
    <div class="rule"></div>
    <h3>Aerospace</h3>
    <p class="desc">Deep network of people, companies, resources</p>
    <ul>
      <li>Metallic Structures</li>
      <li>Fluid Conveyance</li>
      <li>Composite Structures</li>
      <li>Surface Treatment</li>
    </ul>
    <h3>Industrial</h3>
    <p class="desc">Companies that share common characteristics with aerospace</p>
    <ul>
      <li>Regulated quality control</li>
      <li>Product certification</li>
      <li>Precision manufacturing</li>
      <li>Engineering driven</li>
    </ul>
    <div class="btn">Read More
      <svg width="10" height="14" viewBox="0 0 10 14"><path d="M2 1l6 6-6 6" fill="none" stroke="#fff" stroke-width="2"/></svg>
    </div>
  </div>
</section>

<section class="partners">
  <h2 class="section-title">Our Partners</h2>
  <div class="rule"></div>
  <p class="lead">Corvin Partners have had P&amp;L responsibilities in LMM Companies - invest<br>with an operational mindset</p>
  <div class="partner-row">
    <div class="partner">Borecraft</div>
    <div class="partner">Holloway</div>
    <div class="partner"><i></i>Ashby Aerospace</div>
    <div class="partner">Tandemline</div>
    <div class="partner">Skyharbor</div>
  </div>
</section>

<footer class="site-footer">&copy; 2017 Corvin Partners | Privacy Policy | User Agreement</footer>

</body>
</html>
```